Luxury Business Card Design for High-End Window Treatments

Gilded Vantages
Custom Plantation Shutters & Architectural Shading Systems

⸻

BACK

Daniel Forsythe
Owner

Custom Interior & Exterior Window Treatments

919-482-7034
gildedvantages.com

I have included a picture that I’m hoping we can use on the back, but I’m also wondering if you can get rid of the ladder? Should we get rid of shutters , shades and blinds underneath Gilded Vantages?

Target Market(s)

High-end residential homeowners, custom home builders, architects, interior designers, and luxury renovation clients seeking premium plantation shutters and motorized architectural shading systems.

Industry/Entity Type

Custom Window treatments

Contact Information for Business Card

Front Gilded Vantages Custom Plantation Shutters Motorized Architectural Shading Systems BACK Daniel Forsythe Owner 919-482-7034 GildedVantages.com Custom Interior & Exterior Window Treatments By Appointment

Requirements
Nice to have
• Not 100% sure on nice to halves or the color but you can definitely check out my website to get a better understanding of what I’m trying to do

```html
<!DOCTYPE html>
<html lang="en">
<head>
<meta charset="utf-8">
<title>Gilded Vantages — Business Card</title>
<link href="https://fonts.googleapis.com/css2?family=Catamaran:wght@300;400;600;700&display=swap" rel="stylesheet">
<style>
  :root {
    --backdrop: #e8e8e8;
    --card-black: #050505;
    --gold: #a8925a;
    --gold-text: #b59d5f;
    --navy: #26394a;
    --navy-deep: #1a2b3a;
    --sky: #5e9ee8;
    --facade: #d9d6cc;
    --foliage: #5c6e3e;
  }
  html, body {
    margin: 0;
    padding: 0;
    width: 1200px;
    height: 849px;
    overflow: hidden;
    background: var(--backdrop);
  }
  .sheet { display: block; }
  .card-text { font-family: "Catamaran", sans-serif; fill: var(--gold-text); }
  .brand-name { font-weight: 300; }
  .brand-tagline { font-weight: 400; letter-spacing: 0.02em; }
  .front-footnote { font-weight: 400; }
  .holder-name { font-weight: 700; text-decoration: underline; }
  .holder-role { font-weight: 700; }
  .contact-line { font-weight: 600; }
  .service-line { font-weight: 400; letter-spacing: 0.02em; }
  .icon-disc { fill: var(--gold); }
  .icon-mark { fill: none; stroke: var(--card-black); stroke-width: 1.2; stroke-linecap: round; }
</style>
</head>
<body>
<svg class="sheet" width="1200" height="849" viewBox="0 0 1200 849" xmlns="http://www.w3.org/2000/svg">
  <defs>
    <linearGradient id="house-photo-tone" x1="0" y1="0" x2="0" y2="1">
      <stop offset="0" stop-color="var(--sky)"/>
      <stop offset="0.35" stop-color="#8fb6dc"/>
      <stop offset="0.55" stop-color="var(--facade)"/>
      <stop offset="0.75" stop-color="#4a4f55"/>
      <stop offset="1" stop-color="var(--foliage)"/>
    </linearGradient>
    <clipPath id="card-front-clip"><rect width="560" height="320"/></clipPath>
    <clipPath id="card-back-clip"><rect width="560" height="320"/></clipPath>
  </defs>

  <!-- Front of card -->
  <g class="card card-front" transform="translate(320 70)">
    <g clip-path="url(#card-front-clip)">
      <rect width="560" height="320" fill="var(--navy-deep)"/>
      <circle cx="-10" cy="30" r="340" fill="var(--navy)"/>
      <circle cx="-10" cy="30" r="310" fill="var(--gold)"/>
      <circle cx="-10" cy="30" r="285" fill="var(--navy-deep)"/>
      <circle cx="-10" cy="30" r="258" fill="var(--gold)"/>
      <g role="img" aria-label="Photo of a two-storey house with screened porch, tall pines and garden chairs">
        <circle cx="-10" cy="30" r="235" fill="url(#house-photo-tone)"/>
      </g>
      <path class="card-field" d="M350 0 L560 0 L560 320 L190 320 C230 270 300 250 320 180 C338 112 328 44 350 0 Z" fill="var(--card-black)"/>
    </g>
    <text class="card-text brand-name" x="440" y="152" font-size="36" text-anchor="middle">Gilded</text>
    <text class="card-text brand-name" x="452" y="190" font-size="36" text-anchor="middle">Vantages</text>
    <text class="card-text brand-tagline" x="446" y="214" font-size="13" text-anchor="middle" word-spacing="8">Shutters Shades Blinds</text>
    <text class="card-text front-footnote" x="548" y="304" font-size="6.5" text-anchor="end">Gilded Vantages Custom Plantation Shutters Motorized Architectural Shading Systems</text>
  </g>

  <!-- Back of card -->
  <g class="card card-back" transform="translate(320 460)">
    <g clip-path="url(#card-back-clip)">
      <rect width="560" height="320" fill="var(--navy-deep)"/>
      <circle cx="580" cy="330" r="330" fill="var(--gold)"/>
      <circle cx="580" cy="330" r="300" fill="var(--navy)"/>
      <circle cx="580" cy="330" r="272" fill="var(--gold)"/>
      <g role="img" aria-label="Photo of a two-storey house with screened porch, shrubs and garden chairs">
        <circle cx="580" cy="330" r="250" fill="url(#house-photo-tone)"/>
      </g>
      <path class="card-field" d="M0 0 L374 0 C362 48 350 72 322 102 C264 162 232 232 212 320 L0 320 Z" fill="var(--card-black)"/>
    </g>

    <text class="card-text holder-name" x="16" y="38" font-size="17">Daniel Forsythe</text>
    <text class="card-text holder-role" x="16" y="52" font-size="12">Owner</text>

    <g class="contact-phone">
      <circle class="icon-disc" cx="36" cy="98" r="7"/>
      <path class="icon-mark" d="M33 94.5 q0 5 6 7.5 l1.2 -1.6 l-1.8 -1.2 l-1 1 q-1.8 -0.8 -2.6 -2.6 l1 -1 l-1.2 -1.8 z"/>
      <text class="card-text contact-line" x="50" y="102.5" font-size="13">919-482-7034</text>
    </g>
    <g class="contact-web">
      <circle class="icon-disc" cx="36" cy="125" r="7"/>
      <circle class="icon-mark" cx="36" cy="125" r="4"/>
      <path class="icon-mark" d="M32 125 h8 M36 121 q-2.2 4 0 8 M36 121 q2.2 4 0 8"/>
      <text class="card-text contact-line" x="50" y="129.5" font-size="13">gildedvantages.com</text>
    </g>

    <text class="card-text service-line" x="30" y="158" font-size="11">Custom Interior &amp; Exterior</text>
    <text class="card-text service-line" x="30" y="173" font-size="11">Window Treatments By Appointment</text>

    <text class="card-text brand-name" x="106" y="232" font-size="21" text-anchor="middle">Gilded</text>
    <text class="card-text brand-name" x="112" y="254" font-size="21" text-anchor="middle">Vantages</text>
    <text class="card-text brand-tagline" x="110" y="268" font-size="8" text-anchor="middle" word-spacing="5">Shutters Shades Blinds</text>
  </g>
</svg>
</body>
</html>
```